TovaLamarpe - Israeli Mental Health Website

We are developing an Israeli website for mental health. The website will be both in English and in Hebrew. We have a logo and would like a website design based on the logo and the logos colors (attached).

Attached is a doc that contains the website requirements.

We would like to have an icon for each of the sidebar categories, an image for each of the pages (including each of the sidebar category pages).

Target Market(s)

Adults 18-80

Industry/Entity Type

Mental Health

Number of Pages Required

5+ page

Font styles to use
Sans Serif

Colors

Designer to choose colors to be used in the design.

```html
<!DOCTYPE html>
<html lang="en">
<head>
<meta charset="utf-8">
<title>TovaLamarpe – Organization for Mental Health</title>
<link rel="stylesheet" href="https://fonts.googleapis.com/css2?family=Bebas+Neue&family=Raleway:wght@400;500;600&display=swap">
<style>
:root{
  --blue:#1f6fc4;
  --green:#4aa63a;
  --ink:#1d1d1d;
  --text:#3a3a3a;
  --icon:#555555;
  --soft:#f5f5f5;
  --soft2:#efefef;
  --white:#ffffff;
  --line:#d9d9d9;
}
*{margin:0;padding:0;box-sizing:border-box}
html,body{width:1200px;height:2757px;overflow:hidden}
body{position:relative;font-family:"Raleway",sans-serif;color:var(--text);background:var(--white)}
.abs{position:absolute}
.display{font-family:"Bebas Neue",sans-serif;color:var(--ink);font-weight:400}
.btn{position:absolute;display:flex;align-items:center;justify-content:center;background:var(--green);color:var(--white);font-size:16px;border-radius:4px;font-weight:500}
.brand{font-weight:600;color:var(--blue)}

.header{left:0;top:0;width:1200px;height:98px;background:var(--white)}
.header .brand{position:absolute;left:0;width:1200px;top:36px;text-align:center;font-size:24px}
.lang{left:960px;top:36px;width:120px;height:27px;border:1.5px solid var(--blue);border-radius:6px;display:flex;align-items:center;gap:8px;padding-left:4px;font-weight:600;font-size:16px}
.lang .sq{width:22px;height:19px;background:var(--blue);border-radius:4px}
.lang .on{color:var(--blue)} .lang .off{color:#9aa8bb}
.nav{left:0;top:98px;width:1200px;height:49px;background:var(--blue);display:flex;align-items:center;padding-left:173px}
.nav a{color:var(--white);font-size:14px;margin-right:53px}

.hero{left:0;top:147px;width:1200px;height:445px;
  background:
   radial-gradient(ellipse 260px 180px at 330px 200px,rgba(214,190,150,.55),transparent 70%),
   radial-gradient(ellipse 220px 160px at 250px 400px,rgba(200,140,60,.45),transparent 70%),
   radial-gradient(ellipse 300px 200px at 560px 330px,rgba(40,40,45,.6),transparent 70%),
   linear-gradient(110deg,#8f8a7e 0%,#6a665c 35%,#4b4b48 65%,#3b3c3e 100%)}
.hero-title{left:660px;width:465px;top:258px;text-align:center;font-size:84px;color:var(--white);line-height:1}
.hero-sub{left:660px;width:465px;top:356px;text-align:center;font-size:28px;color:var(--white)}

.intro{left:0;top:592px;width:1200px;height:683px;background:var(--soft)}
.side{left:27px;top:626px;width:365px;height:557px;background:var(--white);border-radius:10px;overflow:hidden}
.side .bar{height:19px;background:var(--green)}
.side ul{list-style:none;margin-top:14px}
.side li{height:37.6px;display:flex;align-items:center;padding-left:21px;font-size:15px;color:var(--ink)}
.side li svg{width:17px;height:17px;margin-right:14px;color:var(--icon);flex:none}
.side li.active{background:var(--soft);color:var(--green);height:44px}
.side li.active svg{color:var(--green)}
.p{font-size:16px;line-height:27.3px;text-align:justify}

.cards{left:0;top:1275px;width:1200px;height:1255px;background:var(--soft2)}
.card{position:absolute;width:458px;height:503px;background:var(--white);border-radius:22px}
.card .ph{position:absolute;left:24px;top:33px;width:405px;height:193px;border-radius:18px}
.card h3{position:absolute;left:35px;top:248px;font-size:42px;line-height:1}
.card .p{position:absolute;left:33px;top:312px;width:392px}
.card .btn{bottom:-14px;height:40px}

.footer{left:0;top:2530px;width:1200px;height:227px;background:var(--white)}
.flinks{left:378px;top:2584px;width:701px;display:flex;justify-content:space-between;font-size:14.5px;color:var(--ink)}
.rule{left:372px;width:707px;height:1px;background:var(--line)}
.small{font-size:14px;color:var(--ink)}
.dot{width:14px;height:14px;border-radius:50%;background:var(--blue)}
</style>
</head>
<body>

<header class="abs header"><div class="brand">TovaLamarpe</div></header>
<div class="abs lang"><span class="sq"></span><span class="on">EN</span><span class="off">|</span><span class="off">HE</span></div>
<nav class="abs nav">
  <a>SMART CHATLINE</a><a>THERAPISTS</a><a>ORGANIZATIONS</a><a>VIDEOS</a><a>CONTACT</a><a>ABOUT</a><a>DONATE</a>
</nav>

<section class="abs hero" role="img" aria-label="Support group sitting in a circle holding hands"></section>
<h1 class="abs display hero-title">TOVA LAMARPE</h1>
<p class="abs hero-sub">Organization for Mental Health</p>
<div class="btn" style="left:822px;top:411px;width:143px;height:39px">Get Started</div>

<section class="abs intro"></section>
<aside class="abs side">
  <div class="bar"></div>
  <ul>
    <li><svg viewBox="0 0 16 16" fill="none" stroke="currentColor" stroke-width="1.4"><path d="M8 14S2 10 2 6a3 3 0 0 1 6-1 3 3 0 0 1 6 1c0 4-6 8-6 8z"/></svg>EMERGENCY MENTAL HELP</li>
    <li><svg viewBox="0 0 16 16" fill="none" stroke="currentColor" stroke-width="1.4"><path d="M8 2C6 6 4 8 4 10.5a4 4 0 0 0 8 0C12 8 10 6 8 2z"/></svg>SUICIDE</li>
    <li><svg viewBox="0 0 16 16" fill="none" stroke="currentColor" stroke-width="1.4"><path d="M8 1.5 2.5 4v4c0 3.5 2.5 5.5 5.5 6.5 3-1 5.5-3 5.5-6.5V4z"/></svg>SEXUAL ASSAULT/VIOLENCE VICTIMS</li>
    <li><svg viewBox="0 0 16 16" fill="none" stroke="currentColor" stroke-width="1.4"><path d="M8 2 14.5 14h-13z"/><path d="M8 6.5v3.5M8 11.8v.4"/></svg>SEXUAL ASSAULT/VIOLENCE ASSAULTERS</li>
    <li><svg viewBox="0 0 16 16" fill="none" stroke="currentColor" stroke-width="1.4"><path d="M9.5 1.5 3.5 9h4l-1 5.5 6-7.5h-4z"/></svg>POST TRAUMA</li>
    <li class="active"><svg viewBox="0 0 16 16" fill="none" stroke="currentColor" stroke-width="1.4"><path d="M4.5 11a3 3 0 0 1 0-6 4 4 0 0 1 7.5 1 2.5 2.5 0 0 1 0 5z"/><path d="M6 13v1.5M9 13v1.5"/></svg>DEPRESSION</li>
    <li><svg viewBox="0 0 16 16" fill="none" stroke="currentColor" stroke-width="1.4"><path d="M1.5 8h2.5l1.5-4 2.5 8 2-6 1.5 2h3"/></svg>ANXIETY</li>
    <li><svg viewBox="0 0 16 16" fill="none" stroke="currentColor" stroke-width="1.4"><rect x="1.5" y="5.5" width="13" height="5" rx="2.5" transform="rotate(-35 8 8)"/><path d="M6.4 5.6l3 4.3"/></svg>ADDICTIONS</li>
    <li><svg viewBox="0 0 16 16" fill="none" stroke="currentColor" stroke-width="1.4"><path d="M12.5 10A5.5 5.5 0 0 1 6 3.5a5 5 0 1 0 6.5 6.5z"/></svg>SLEEP DISORDERS</li>
    <li><svg viewBox="0 0 16 16" fill="none" stroke="currentColor" stroke-width="1.4"><circle cx="8" cy="8" r="4"/><path d="M1.5 2v4a1 1 0 0 0 2 0V2M2.5 6v8M14 2v12"/></svg>EATING DISORDERS</li>
    <li><svg viewBox="0 0 16 16" fill="none" stroke="currentColor" stroke-width="1.4"><circle cx="8" cy="8" r="6"/><path d="M10 5.5H7a1.3 1.3 0 0 0 0 2.5h2a1.3 1.3 0 0 1 0 2.5H6M8 4v1.5M8 10.5V12"/></svg>FINANCIAL PROBLEMS</li>
    <li><svg viewBox="0 0 16 16" fill="none" stroke="currentColor" stroke-width="1.4"><circle cx="5" cy="4" r="2"/><path d="M2 14v-4a3 3 0 0 1 6 0v4"/><circle cx="11.5" cy="8" r="1.5"/><path d="M9.5 14v-2a2 2 0 0 1 4 0v2"/></svg>PARENTHOOD</li>
    <li><svg viewBox="0 0 16 16" fill="none" stroke="currentColor" stroke-width="1.4"><circle cx="6" cy="9" r="4"/><circle cx="10" cy="7" r="4"/></svg>RELATIONSHIP</li>
  </ul>
</aside>

<h2 class="abs display" style="left:441px;top:664px;font-size:40px">WELCOME TO TOVA LAMARPE</h2>
<p class="abs p" style="left:443px;top:727px;width:626px">Lorem ipsum dolor sit amet, consectetur adipiscing elit, sed do eiusmod tempor incididunt ut labore et dolore magna aliqua. Quis ipsum suspendisse ultrices gravida. Risus commodo viverra maecenas accumsan lacus vel facilisis. Lorem ipsum dolor sit amet, consectetur adipiscing elit, sed do eiusmod tempor incididunt ut labore et dolore magna aliqua. Quis ipsum suspendisse ultrices gravida. Risus commodo viverra maecenas accumsan lacus vel facilisis.</p>

<div class="abs" role="img" aria-label="Distressed man in a hood holding his head in his hands" style="left:443px;top:941px;width:256px;height:242px;border-radius:12px;background:radial-gradient(ellipse 90px 80px at 128px 80px,#c3d4df,transparent 75%),radial-gradient(ellipse 110px 50px at 128px 200px,#c99f86,transparent 75%),linear-gradient(160deg,#8fb2c9,#3f7196)"></div>
<h2 class="abs display" style="left:732px;top:937px;font-size:40px">EMERGENCY MENTAL HELP</h2>
<p class="abs p" style="left:732px;top:988px;width:347px">Lorem ipsum dolor sit amet, consectetur adipiscing elit, sed do eiusmod tempor incididunt ut labore et dolore magna et dolore magna aliqua. Quis ipsum suspendisse ultrices gravida.</p>
<div class="btn" style="left:733px;top:1139px;width:331px;height:39px">More options for Emergency Mental Help</div>

<section class="abs cards"></section>

<div class="card" style="left:120px;top:1357px">
  <div class="ph" role="img" aria-label="Hand holding a smartphone in front of a laptop" style="background:radial-gradient(ellipse 80px 90px at 290px 90px,#e9ecea,transparent 75%),radial-gradient(ellipse 160px 60px at 110px 150px,#3a3d3f,transparent 75%),linear-gradient(120deg,#4f6a63,#9aa1a0)"></div>
  <h3 class="display">SMART CHATLINE</h3>
  <p class="p">Lorem ipsum dolor sit amet, consectetur adipiscing elit, sed do eiusmod tempor incididunt ut labore et dolore magna aliqua. Quis ipsum suspendisse ultrices gravida. Risus commodo viverra maecenas accumsan lacus vel facilisis.</p>
  <div class="btn" style="left:142px;width:178px;gap:8px"><span style="width:26px;height:26px;border-radius:50%;background:var(--white)"></span>+(1) 555 010 2030</div>
</div>

<div class="card" style="left:622px;top:1357px">
  <div class="ph" role="img" aria-label="Therapist in session with a client on a sofa" style="background:radial-gradient(ellipse 70px 90px at 80px 100px,#e7d8bf,transparent 75%),radial-gradient(ellipse 80px 90px at 290px 110px,#c9a893,transparent 75%),linear-gradient(120deg,#cfd3d4,#ebe8e4)"></div>
  <h3 class="display">THERAPISTS</h3>
  <p class="p">Lorem ipsum dolor sit amet, consectetur adipiscing elit, sed do eiusmod tempor incididunt ut labore et dolore magna aliqua. Quis ipsum suspendisse ultrices gravida. Risus commodo viverra maecenas accumsan lacus vel facilisis.</p>
  <div class="btn" style="left:151px;width:169px">Find Therapists</div>
</div>

<div class="card" style="left:120px;top:1914px">
  <div class="ph" role="img" aria-label="Team assembling puzzle pieces on a wooden table" style="background:radial-gradient(ellipse 130px 70px at 200px 95px,#ddd8cf,transparent 75%),radial-gradient(circle 18px at 190px 95px,#d9302a,transparent 100%),linear-gradient(120deg,#4f463c,#8a7c6b)"></div>
  <h3 class="display">ORGANIZATIONS</h3>
  <p class="p">Lorem ipsum dolor sit amet, consectetur adipiscing elit, sed do eiusmod tempor incididunt ut labore et dolore magna aliqua. Quis ipsum suspendisse ultrices gravida. Risus commodo viverra maecenas accumsan lacus vel facilisis.</p>
  <div class="btn" style="left:145px;width:169px">Find Organizations</div>
</div>

<div class="card" style="left:622px;top:1914px">
  <div class="ph" role="img" aria-label="Video thumbnail of a woman talking on a sofa" style="background:radial-gradient(ellipse 90px 100px at 140px 110px,#f1efec,transparent 75%),radial-gradient(ellipse 70px 60px at 240px 160px,#c89a45,transparent 75%),radial-gradient(ellipse 90px 100px at 370px 60px,#3d5a3a,transparent 75%),linear-gradient(120deg,#6f5a48,#d8d4cc)"></div>
  <svg class="abs" style="left:200px;top:70px" width="52" height="52" viewBox="0 0 52 52"><circle cx="26" cy="26" r="26" fill="#fff"/><path d="M20 16 L36 26 L20 36Z" fill="#4aa63a"/></svg>
  <h3 class="display">VIDEOS</h3>
  <p class="p">Lorem ipsum dolor sit amet, consectetur adipiscing elit, sed do eiusmod tempor incididunt ut labore et dolore magna aliqua. Quis ipsum suspendisse ultrices gravida. Risus commodo viverra maecenas accumsan lacus vel facilisis.</p>
  <div class="btn" style="left:144px;width:169px">Video Library</div>
</div>

<div class="abs" style="left:1116px;top:2482px;width:58px;height:58px;border-radius:50%;background:var(--green);box-shadow:0 6px 10px rgba(0,0,0,.15)"></div>

<footer class="abs footer"></footer>
<div class="abs brand" style="left:120px;top:2640px;width:200px;text-align:center;font-size:26px">TovaLamarpe</div>
<div class="abs flinks"><span>Smart Chatline</span><span>Therapists</span><span>Organizations</span><span>Videos</span><span>Contact</span><span>About</span><span>Donate</span></div>
<div class="abs rule" style="top:2623px"></div>
<svg class="abs" style="left:375px;top:2647px" width="12" height="16" viewBox="0 0 12 16"><path d="M6 0C2.7 0 0 2.6 0 5.9 0 10 6 16 6 16s6-6 6-10.1C12 2.6 9.3 0 6 0z" fill="#1f6fc4"/><circle cx="6" cy="6" r="2.2" fill="#fff"/></svg>
<div class="abs small" style="left:398px;top:2647px">12, Cedar Lane, Hadar - 340071</div>
<svg class="abs" style="left:637px;top:2651px" width="14" height="10" viewBox="0 0 14 10"><rect width="14" height="10" rx="1" fill="#1f6fc4"/><path d="M0 0 L7 6 L14 0" stroke="#fff" fill="none"/></svg>
<div class="abs small" style="left:661px;top:2647px">hello@tovalamarpe-care.org</div>
<div class="abs small" style="left:903px;top:2645px">Privacy Policy</div>
<div class="abs small" style="left:1040px;top:2645px">Terms</div>
<div class="abs rule" style="top:2683px"></div>
<div class="abs" style="left:375px;top:2705px;font-size:12px;color:var(--ink)">TovaLamarpe - Organization for Mental Health ©2023 | All Rights Reserved</div>
<div class="abs dot" style="left:1003px;top:2707px"></div>
<div class="abs dot" style="left:1033px;top:2707px"></div>
<div class="abs dot" style="left:1062px;top:2707px"></div>
<div class="abs" style="left:1151px;top:2707px;font-size:12px;color:var(--ink)">C54</div>

</body>
</html>
```